Need a solid log.
My company Sales: OrbiqView, Plate Linkway, Valtor Internet
Design and installation of WI_FI systems.
Fulfillment company for installations in the Electronics industry

Industry/Entity Type

Electronics

Contact Information for Business Card

Mark T. Doverly
President
Phone: 256.418.2096 Cell: 256.7193058 mtdoverly@brightlinkradio.biz
Brightlink Radio Systems
Marlowe Falls, KY. 35871

```html
<!DOCTYPE html>
<html lang="en">
<head>
<meta charset="utf-8">
<title>Brightlink Radio Systems — Business Card</title>
<link rel="stylesheet" href="https://fonts.googleapis.com/css2?family=Orbitron:wght@700&family=Roboto+Condensed:wght@700&family=Oswald:wght@300;500&family=Aldrich&display=swap">
<style>
  :root {
    --card-edge: #0d0c09;
    --bg-dark: #1e1c15;
    --bg-olive: #2d2b22;
    --bg-mid: #4a4844;
    --bg-light: #565452;
    --ink: #ffffff;
    --ink-soft: #ececea;
    --outline: #2a2824;
    --deco-core: #3b3935;
    --deco-edge: rgba(40, 38, 33, 0);
  }
  html, body {
    margin: 0;
    padding: 0;
    width: 1200px;
    height: 663px;
    overflow: hidden;
    background: #ffffff;
  }
  .card {
    position: relative;
    box-sizing: border-box;
    width: 1200px;
    height: 663px;
    border: 5px solid var(--card-edge);
    border-radius: 48px;
    overflow: hidden;
    background: linear-gradient(118deg,
      var(--bg-olive) 0%,
      var(--bg-mid) 30%,
      var(--bg-light) 52%,
      var(--bg-mid) 68%,
      var(--bg-dark) 92%);
  }
  .identity {
    position: absolute;
    right: calc(1200px - 458px);
    top: 164px;
    text-align: right;
  }
  .identity__name {
    margin: 0;
    font-family: "Orbitron", sans-serif;
    font-weight: 700;
    font-size: 29px;
    letter-spacing: 0.5px;
    line-height: 1;
    color: var(--ink);
    text-shadow:
      2px 0 0 var(--outline), -2px 0 0 var(--outline),
      0 2px 0 var(--outline), 0 -2px 0 var(--outline);
  }
  .identity__title {
    margin: 8px 0 0;
    font-family: "Roboto Condensed", sans-serif;
    font-weight: 700;
    font-size: 28px;
    line-height: 1;
    color: var(--ink);
  }
  .divider {
    position: absolute;
    left: 489px;
    top: 108px;
    width: 6px;
    height: 210px;
    background: var(--ink);
  }
  .contacts {
    position: absolute;
    left: 520px;
    top: 122px;
    margin: 0;
    padding: 0;
    list-style: none;
  }
  .contacts__item {
    display: flex;
    align-items: center;
    height: 44px;
    margin-bottom: 24px;
    font-family: "Oswald", sans-serif;
    font-weight: 300;
    font-size: 31px;
    color: var(--ink-soft);
  }
  .contacts__icon {
    width: 40px;
    height: 44px;
    margin-right: 10px;
    flex: none;
  }
  .contacts__item--email { font-size: 33px; }
  .company {
    position: absolute;
    left: 48px;
    top: 520px;
  }
  .company__name {
    margin: 0;
    font-family: "Oswald", sans-serif;
    font-weight: 500;
    font-size: 38px;
    line-height: 1;
    color: var(--ink);
  }
  .company__address {
    margin: 14px 0 0;
    text-align: right;
    font-family: "Aldrich", sans-serif;
    font-size: 19px;
    letter-spacing: 1px;
    color: var(--ink-soft);
  }
  .decor-arc {
    position: absolute;
    left: 690px;
    top: 66px;
    width: 480px;
    height: 580px;
  }
</style>
</head>
<body>
  <div class="card">
    <svg class="decor-arc" viewBox="0 0 480 580" role="img" aria-label="Decorative arc of shaded dots sweeping around the right side of the card">
      <defs>
        <radialGradient id="decor-glow" cx="0.6" cy="0.5" r="0.55">
          <stop offset="0" stop-color="var(--deco-core)"/>
          <stop offset="1" stop-color="var(--deco-edge)"/>
        </radialGradient>
      </defs>
      <rect x="0" y="0" width="480" height="580" fill="url(#decor-glow)"/>
    </svg>

    <div class="identity">
      <p class="identity__name">MARK T. DOVERLY</p>
      <p class="identity__title">President</p>
    </div>

    <div class="divider"></div>

    <ul class="contacts">
      <li class="contacts__item">
        <svg class="contacts__icon" viewBox="0 0 40 44" aria-hidden="true">
          <path d="M14 4 h6 v10 h-5 c-2 5 -2 11 0 16 h5 v10 h-6 c-7 -8 -7 -28 0 -36 z" fill="var(--ink)"/>
        </svg>
        <span>256.418.2096</span>
      </li>
      <li class="contacts__item">
        <svg class="contacts__icon" viewBox="0 0 40 44" aria-hidden="true">
          <rect x="8" y="2" width="24" height="40" rx="3" fill="var(--ink)"/>
          <rect x="11" y="7" width="18" height="27" fill="var(--outline)"/>
          <circle cx="20" cy="38" r="1.6" fill="var(--outline)"/>
        </svg>
        <span>256.7193058</span>
      </li>
      <li class="contacts__item contacts__item--email">
        <svg class="contacts__icon" viewBox="0 0 40 44" aria-hidden="true">
          <path d="M2 20 L20 8 L38 20 V40 H2 Z" fill="var(--ink)"/>
          <rect x="9" y="12" width="22" height="18" fill="var(--ink)" stroke="var(--outline)" stroke-width="1.5"/>
          <text x="20" y="26" text-anchor="middle" font-family="Arial, sans-serif" font-size="13" font-weight="700" fill="var(--outline)">@</text>
          <path d="M2 20 L20 32 L38 20 M2 40 L17 29 M38 40 L23 29" fill="none" stroke="var(--outline)" stroke-width="2"/>
        </svg>
        <span>mtdoverly@brightlinkradio.biz</span>
      </li>
    </ul>

    <div class="company">
      <p class="company__name">Brightlink Radio Systems</p>
      <p class="company__address">Marlowe Falls, KY. 35871</p>
    </div>
  </div>
</body>
</html>
```